KESTREL REFRIGERATION Business Card design

We are looking for a business card design front and back. We would like our logo only on the front with all other details on the rear.
Rear should include name, email address and two phone numbers. Similar to the attachment.
Smart and bright.
Looking for a matt finish on all of the card but the logo to be gloss and slightly proud.

Contact Information for Business Card

Name - Gavin Holloway
Director
Phone - 0867302948
0417259083
email - gavin@kestrelrefrigeration.com.au
website - kestrelrefrigeration.com.au

Font styles to use
Serif

Requirements
Must have
• Colours from our logo. icons for phone, email etc.

```html
<!DOCTYPE html>
<html lang="en">
<head>
<meta charset="utf-8">
<title>Kestrel Refrigeration Business Card</title>
<link href="https://fonts.googleapis.com/css2?family=Open+Sans:wght@400;600;700;800&display=swap" rel="stylesheet">
<style>
  :root {
    --backdrop: #4b4b4d;
    --brand-purple: #56407a;
    --brand-lime: #a9d46b;
    --card-white: #ffffff;
    --divider: #8a8a8a;
  }
  * { box-sizing: border-box; margin: 0; padding: 0; }
  html, body {
    width: 1200px;
    height: 977px;
    overflow: hidden;
    background: var(--backdrop);
    font-family: "Open Sans", Arial, sans-serif;
  }
  .canvas {
    width: 1200px;
    height: 977px;
    display: flex;
    align-items: center;
    justify-content: center;
    gap: 40px;
  }
  .card {
    width: 540px;
    height: 309px;
    border-radius: 3px;
    box-shadow: 0 10px 24px rgba(0,0,0,0.35);
    position: relative;
  }
  .card-front {
    background: var(--brand-purple);
    display: flex;
    align-items: center;
    justify-content: center;
  }
  .wordmark {
    display: flex;
    align-items: center;
    gap: 10px;
    font-weight: 800;
    letter-spacing: 0.02em;
    line-height: 1;
    text-align: center;
  }
  .wordmark-dot {
    width: 16px;
    height: 16px;
    border-radius: 50%;
    flex: none;
  }
  .card-front .wordmark { color: var(--brand-lime); font-size: 26px; }
  .card-front .wordmark-dot { background: var(--brand-lime); }

  .card-back {
    background: var(--card-white);
    display: grid;
    grid-template-columns: 1fr 1px 1fr;
    align-items: center;
  }
  .back-brand {
    display: flex;
    justify-content: center;
  }
  .card-back .wordmark {
    color: var(--brand-purple);
    font-size: 15px;
    flex-direction: column;
    gap: 6px;
  }
  .card-back .wordmark-dot { background: var(--brand-lime); width: 14px; height: 14px; }
  .divider {
    width: 1px;
    height: 210px;
    background: linear-gradient(to bottom, transparent, var(--divider) 30%, var(--divider) 70%, transparent);
  }
  .contact {
    padding-left: 26px;
    color: var(--brand-purple);
  }
  .contact-name {
    font-size: 19px;
    font-weight: 700;
  }
  .contact-role {
    font-size: 11px;
    color: #333;
    margin: 2px 0 14px 10px;
  }
  .contact-list {
    list-style: none;
    margin-left: 10px;
  }
  .contact-list li {
    display: flex;
    align-items: center;
    gap: 7px;
    font-size: 11.5px;
    line-height: 18px;
  }
  .contact-icon {
    width: 10px;
    height: 10px;
    fill: var(--brand-purple);
    flex: none;
  }
</style>
</head>
<body>
<main class="canvas">
  <section class="card card-front" aria-label="Card front">
    <div class="wordmark"><span class="wordmark-dot"></span>KESTREL REFRIGERATION</div>
  </section>

  <section class="card card-back" aria-label="Card back">
    <div class="back-brand">
      <div class="wordmark"><span class="wordmark-dot"></span>KESTREL REFRIGERATION</div>
    </div>
    <div class="divider"></div>
    <div class="contact">
      <h1 class="contact-name">Gavin Holloway</h1>
      <p class="contact-role">Director</p>
      <ul class="contact-list">
        <li>
          <svg class="contact-icon" viewBox="0 0 24 24" aria-hidden="true"><path d="M6.6 10.8c1.4 2.8 3.8 5.1 6.6 6.6l2.2-2.2c.3-.3.7-.4 1-.2 1.1.4 2.3.6 3.6.6.6 0 1 .4 1 1V20c0 .6-.4 1-1 1C10.6 21 3 13.4 3 4c0-.6.4-1 1-1h3.5c.6 0 1 .4 1 1 0 1.3.2 2.5.6 3.6.1.3 0 .7-.2 1z"/></svg>
          <span>0867302948</span>
        </li>
        <li>
          <svg class="contact-icon" viewBox="0 0 24 24" aria-hidden="true"><path d="M6.6 10.8c1.4 2.8 3.8 5.1 6.6 6.6l2.2-2.2c.3-.3.7-.4 1-.2 1.1.4 2.3.6 3.6.6.6 0 1 .4 1 1V20c0 .6-.4 1-1 1C10.6 21 3 13.4 3 4c0-.6.4-1 1-1h3.5c.6 0 1 .4 1 1 0 1.3.2 2.5.6 3.6.1.3 0 .7-.2 1z"/></svg>
          <span>0417259083</span>
        </li>
        <li>
          <svg class="contact-icon" viewBox="0 0 24 24" aria-hidden="true"><path d="M2 5h20v14H2z M2 5l10 8 10-8" fill="none" stroke="#56407a" stroke-width="0"/><path d="M2 5h20v2l-10 7L2 7z"/><path d="M2 9l10 7 10-7v10H2z"/></svg>
          <span>gavin@kestrelrefrigeration.com.au</span>
        </li>
        <li>
          <svg class="contact-icon" viewBox="0 0 24 24" aria-hidden="true"><circle cx="12" cy="12" r="10" fill="none" stroke="#56407a" stroke-width="2.5"/><circle cx="12" cy="12" r="4"/></svg>
          <span>kestrelrefrigeration.com.au</span>
        </li>
      </ul>
    </div>
  </section>
</main>
</body>
</html>
```